Business Card Design for an Investment Company

We need a business card design for our private investment company, called Ashbourne Partners. Ashbourne Partners is an investments partnership that aims to acquire shares in listed companies with a view to influencing those companies through active dialogue in order to improve their value. We need designs that use the logo colors (blue, grey, white), we need both English and Arabic on the business cards (can be on one side or 2 sides). The final logo should communicate professionalism, conservatism (nothing too fancy or too cheesy), that we are smart, conservative and old school.

Target Market(s)

Investment companies

Industry/Entity Type

Investment

Contact Information for Business Card

Khalid Yousef Rumaithi
Senior Executive Officer

Palm Terrace 07, Level 3, Office 215/12
HLMZ

+9714987650
krumaithi@ashbournepartners.com
www.ashbournepartners.com

Requirements
Must have
• Logo to be placed on the left hand side of the business card
• for the Arabic, we only need to have the name and title so it can be accomodated on one side so we can have the other side with full color and logo. The arabic that needs to be used is the below:
• خالد يوسف الرميثي
• المدير التنفيدي

```html
<!DOCTYPE html>
<html lang="en">
<head>
<meta charset="utf-8">
<title>Ashbourne Partners – Business Cards</title>
<link href="https://fonts.googleapis.com/css2?family=Roboto:wght@300;400;500;700&family=Tajawal:wght@400;500;700&display=swap" rel="stylesheet">
<style>
  :root {
    --page: #e6e6e8;
    --card: #1f1f22;
    --card-hi: #2a2a2e;
    --blue: #1a78c2;
    --silver: #cfd0d2;
    --white: #f2f2f2;
    --rule: #2f6fa3;
    --ink-dark: #1f1f22;
  }
  * { margin: 0; padding: 0; box-sizing: border-box; }
  html, body { width: 1200px; height: 930px; overflow: hidden; }
  body {
    background: var(--page);
    font-family: "Roboto", Arial, sans-serif;
    position: relative;
  }
  .card {
    position: absolute;
    left: 250px;
    width: 700px;
    height: 400px;
    border-radius: 22px;
    overflow: hidden;
    background: linear-gradient(160deg, var(--card-hi) 0%, var(--card) 55%, #1a1a1c 100%);
    color: var(--white);
  }
  .card--arabic { top: 50px; }
  .card--english { top: 480px; }

  .card__wave { position: absolute; inset: 0; width: 700px; height: 400px; }

  .brand {
    position: absolute;
    left: 70px;
    top: 205px;
    display: flex;
    align-items: center;
    gap: 12px;
  }
  .brand__square { width: 22px; height: 22px; background: var(--blue); }
  .brand__name {
    font-family: "Roboto", Arial, sans-serif;
    font-weight: 500;
    font-size: 30px;
    color: var(--blue);
    letter-spacing: 0.2px;
  }

  .card__rule {
    position: absolute;
    left: 392px;
    top: 56px;
    width: 1px;
    height: 190px;
    background: var(--rule);
  }
  .details {
    position: absolute;
    left: 410px;
    top: 52px;
    width: 270px;
    font-size: 14px;
    line-height: 1.3;
  }
  .details__name { font-size: 17px; margin-bottom: 2px; }
  .details__name .first { color: var(--blue); font-weight: 700; }
  .details__title { margin-bottom: 12px; }
  .details__address { margin-bottom: 12px; }
  .contact { list-style: none; font-size: 13.5px; }
  .contact li { display: flex; align-items: center; gap: 8px; }
  .contact svg { width: 12px; height: 12px; flex: none; }
  .contact .accent { color: var(--blue); }

  .details--arabic {
    font-family: "Tajawal", Arial, sans-serif;
    direction: rtl;
    text-align: right;
    font-size: 15px;
  }
  .details--arabic .details__name { color: var(--blue); font-weight: 700; }
  .details--arabic .contact { direction: ltr; text-align: left; font-family: "Roboto", Arial, sans-serif; }
</style>
</head>
<body>

  <!-- Arabic side -->
  <section class="card card--arabic">
    <svg class="card__wave" viewBox="0 0 700 400" aria-hidden="true">
      <path d="M0 390 C170 384 280 336 400 296 C520 258 610 248 700 246 L700 400 L0 400 Z" fill="var(--blue)"/>
      <path d="M0 380 C170 374 280 324 400 283 C520 245 610 236 700 234" fill="none" stroke="var(--silver)" stroke-width="3"/>
    </svg>
    <div class="brand">
      <span class="brand__square"></span>
      <span class="brand__name">Ashbourne Partners</span>
    </div>
    <div class="card__rule"></div>
    <div class="details details--arabic" lang="ar">
      <p class="details__name">خالد يوسف الرميثي</p>
      <p class="details__title">المدير التنفيدي</p>
      <p class="details__address">تراس النخيل 07، المستوى 3،<br>مكتب 215/12 HLMZ</p>
      <ul class="contact">
        <li><svg viewBox="0 0 12 12"><rect x="3" y="1" width="6" height="10" rx="1" fill="none" stroke="var(--blue)" stroke-width="1.3"/></svg>+9714987650</li>
        <li><svg viewBox="0 0 12 12"><rect x="1" y="2.5" width="10" height="7" fill="var(--blue)"/><path d="M1 3 L6 7 L11 3" fill="none" stroke="var(--ink-dark)" stroke-width="1"/></svg>krumaithi@ashbournepartners.com</li>
        <li><svg viewBox="0 0 12 12"><circle cx="5" cy="5" r="3.5" fill="none" stroke="var(--blue)" stroke-width="1.5"/><path d="M7.5 7.5 L11 11" stroke="var(--blue)" stroke-width="1.8"/></svg>www.ashbournepartners.com</li>
      </ul>
    </div>
  </section>

  <!-- English side -->
  <section class="card card--english">
    <svg class="card__wave" viewBox="0 0 700 400" aria-hidden="true">
      <path d="M0 390 C170 384 280 336 400 296 C520 258 610 248 700 246 L700 400 L0 400 Z" fill="var(--blue)"/>
      <path d="M0 380 C170 374 280 324 400 283 C520 245 610 236 700 234" fill="none" stroke="var(--silver)" stroke-width="3"/>
    </svg>
    <div class="brand">
      <span class="brand__square"></span>
      <span class="brand__name">Ashbourne Partners</span>
    </div>
    <div class="card__rule"></div>
    <div class="details">
      <p class="details__name"><span class="first">Khalid</span> Yousef Rumaithi</p>
      <p class="details__title">Senior Executive Officer</p>
      <p class="details__address">Palm Terrace 07, Level 3,<br>Office 215/12 HLMZ</p>
      <ul class="contact">
        <li><svg viewBox="0 0 12 12"><rect x="3" y="1" width="6" height="10" rx="1" fill="none" stroke="var(--blue)" stroke-width="1.3"/></svg>+9714987650</li>
        <li><svg viewBox="0 0 12 12"><rect x="1" y="2.5" width="10" height="7" fill="var(--blue)"/><path d="M1 3 L6 7 L11 3" fill="none" stroke="var(--ink-dark)" stroke-width="1"/></svg>krumaithi@ashbournepartners.com</li>
        <li><svg viewBox="0 0 12 12"><circle cx="5" cy="5" r="3.5" fill="none" stroke="var(--blue)" stroke-width="1.5"/><path d="M7.5 7.5 L11 11" stroke="var(--blue)" stroke-width="1.8"/></svg><span>www.<span class="accent">ashbournepartners</span>.com</span></li>
      </ul>
    </div>
  </section>

</body>
</html>
```